Business Website Re-design, Sharepoint, Office 365

Re-design of our existing Office 365 public website http://www.ridgelinevantek.example. New site must use SharePoint and be compatible with Office 365 Hosting. A preliminary site layout and design is provided but creative suggestions and alternatives will be considered. Please see our attached power point presentation for details on the layout, and site design we are looking for.

Target Market(s)

Industrial Automation

Industry/Entity Type

Business

Coding

Coded - Design and coding required

Number of Pages Required

5+ page

Font styles to use
Serif
Sans Serif

Requirements
Must have
• SharePoint & Office 365 Compatible

```html
<!DOCTYPE html>
<html lang="en">
<head>
<meta charset="utf-8">
<title>Ridgeline Vantek Controls</title>
<link href="https://fonts.googleapis.com/css2?family=Montserrat:wght@400;600&family=Open+Sans:ital,wght@0,400;0,600;1,400&display=swap" rel="stylesheet">
<style>
:root{
  --orange:#f04a1d;
  --orange-dark:#e03b12;
  --ink:#222;
  --text:#333;
  --muted:#6b6b6b;
  --rule:#dcdcdc;
  --white:#fff;
}
*{margin:0;padding:0;box-sizing:border-box}
html,body{width:782px;height:1200px;overflow:hidden;background:var(--white)}
body{position:relative;font-family:"Open Sans",Arial,sans-serif;color:var(--text)}
.abs{position:absolute}
a{color:inherit;text-decoration:none}

.site-header{position:absolute;left:0;top:0;width:782px;height:118px;border-bottom:2px solid #e6e6e6}
.brand{left:42px;top:44px;width:150px;text-align:left}
.brand-name{font-family:"Montserrat",sans-serif;font-weight:600;font-size:17px;color:var(--orange);letter-spacing:1px;display:flex;align-items:center;gap:6px}
.brand-name .mark{width:14px;height:14px;background:var(--orange);border-radius:50%}
.brand-sub{font-size:7.5px;letter-spacing:3px;color:#555;margin-top:3px}
.brand-phone{font-size:8px;font-weight:600;color:var(--orange);letter-spacing:.5px;margin-top:4px}
.portal-links{right:38px;top:50px;font-size:10px;color:var(--ink)}
.portal-links span{margin:0 9px}
.main-nav{right:38px;top:87px;display:flex;gap:20px;font-size:10px;color:var(--ink)}
.main-nav .active{color:var(--orange)}

.hero-band{left:0;top:118px;width:782px;height:221px;background:linear-gradient(var(--orange-dark),var(--orange))}
.hero-frame{left:39px;top:149px;width:704px;height:280px;background:var(--white);border:1px solid #ccc;box-shadow:0 1px 3px rgba(0,0,0,.25);padding:3px}
.hero-photo{width:100%;height:100%;background:linear-gradient(100deg,#b9a56a 0%,#8d8a6d 35%,#a8b2b6 60%,#c85a33 85%,#b33a1c 100%);position:relative}
.hero-caption{left:47px;top:76px;width:246px;height:136px;background:rgba(70,70,70,.78);padding:16px 14px;color:var(--white)}
.hero-kicker{font-size:13px;letter-spacing:.3px}
.hero-title{font-family:"Montserrat",sans-serif;font-weight:600;font-size:22px;margin-top:3px;white-space:nowrap}
.hero-text{font-size:7.5px;line-height:1.25;margin-top:8px;padding-left:2px}
.btn-small{display:inline-block;background:var(--orange);color:var(--white);font-size:7.5px;padding:7px 8px;margin-top:9px;border-radius:2px}
.hero-dots{left:342px;top:255px;display:flex;gap:10px}
.hero-dots i{width:8px;height:8px;border-radius:50%;background:rgba(255,255,255,.6)}
.hero-dots i.on{background:var(--white)}

.section-title{font-family:"Montserrat",sans-serif;font-weight:400;font-size:22px;color:var(--ink)}
.welcome-title{left:0;width:782px;top:458px;text-align:center}
.welcome-text{left:40px;width:702px;top:497px;text-align:center;font-size:8.5px;line-height:1.7;color:var(--muted)}
.btn{left:352px;top:556px;width:77px;height:30px;background:var(--orange);color:var(--white);font-size:11px;font-weight:600;text-align:center;line-height:30px;border-radius:2px}

.services-title{left:39px;top:612px}
.carousel-arrows{left:705px;top:616px}
.service-card{top:661px;width:166px;height:163px;background:linear-gradient(#fff 80%,#eee)}
.service-photo{height:114px}
.service-label{height:37px;background:var(--orange);color:var(--white);font-size:11.5px;padding:12px 11px 0;letter-spacing:.2px}

.testimonial-title{left:0;width:782px;top:847px;text-align:center}
.quote-mark{left:56px;top:890px}
.testimonial-text{left:64px;width:656px;top:903px;text-align:center;text-indent:36px;font-size:8.5px;line-height:1.72;color:var(--text)}
.testimonial-author{left:0;width:782px;top:962px;text-align:center;font-size:9.5px;font-style:italic;color:var(--ink)}

.rule-thick{left:39px;top:995px;width:704px;height:3px;background:#e3e3e3}
.footer-heading{top:1016px;font-family:"Montserrat",sans-serif;font-weight:400;font-size:13.5px;color:#333}
.footer-list{top:1047px;list-style:none;font-size:8px;line-height:14.4px;color:var(--muted);text-transform:uppercase}
.contact-text{left:475px;top:1047px;width:150px;font-size:8.5px;line-height:1.7;color:var(--muted)}
.contact-phone{left:475px;top:1088px;font-size:11px;font-weight:600;color:var(--ink)}
.social{left:657px;top:1049px;list-style:none;font-size:8.5px;color:var(--muted)}
.social li{display:flex;align-items:center;gap:8px;height:18px}
.social li i{width:10px;height:10px;border-radius:50%;background:#888}
.rule-thin{left:39px;top:1141px;width:704px;height:1px;background:var(--rule)}
.footer-nav{left:0;width:782px;top:1152px;display:flex;justify-content:center;gap:18px;font-size:8.5px;color:var(--ink)}
.copyright{left:0;width:782px;top:1170px;text-align:center;font-size:8.5px;color:var(--ink)}
</style>
</head>
<body>

<header class="site-header">
  <a class="abs brand" href="http://www.ridgelinevantek.example">
    <div class="brand-name"><span class="mark"></span>RIDGELINE</div>
    <div class="brand-sub">VANTEK CONTROLS</div>
    <div class="brand-phone">TOLL FREE 1-800-555-0142</div>
  </a>
  <div class="abs portal-links">Canadian Fieldora<span>|</span>USA Fieldora</div>
  <nav class="abs main-nav">
    <a class="active">Home</a><a>Services</a><a>Products</a><a>Equipment</a><a>News</a><a>About us</a><a>Contact us</a><a>Remote Support</a>
  </nav>
</header>

<div class="abs hero-band"></div>
<div class="abs hero-frame">
  <div class="hero-photo" role="img" aria-label="Construction worker in orange hard hat and ear defenders at an industrial site">
    <div class="abs hero-caption">
      <div class="hero-kicker">CONSTRUCTION</div>
      <div class="hero-title">Realize your project</div>
      <p class="hero-text">Nemo enim ipsam voluptatem quia voluptas sit asper-natur aut odit aut fugit.</p>
      <a class="btn-small">Read More</a>
    </div>
    <div class="abs hero-dots"><i></i><i class="on"></i><i></i></div>
  </div>
</div>

<h1 class="abs section-title welcome-title">Welcome To&nbsp; Ridgelinevantek</h1>
<p class="abs welcome-text">Ridgeline Vantek Controls Ltd. was established in Ridgeton, Alberta in 2006 to accommodate the demanding and ever-changing needs of the oil, gas and petrochemical industry. Since then we have developed and maintained relationships with our customers with our goal of “rising above the rest”. Our highly trained and qualified team of journeyman and apprentice instrument technicians and electricians strive to not only meet, but exceed all expectations.</p>
<a class="abs btn">Read More</a>

<h2 class="abs section-title services-title">Our Services</h2>
<svg class="abs carousel-arrows" width="39" height="20" viewBox="0 0 39 20" aria-hidden="true">
  <g fill="none" stroke="#222" stroke-width="2.2">
    <circle cx="10" cy="10" r="8.5"/><circle cx="29" cy="10" r="8.5"/>
    <path d="M15 10H6M9 6.5 5.5 10 9 13.5"/><path d="M24 10h9M30 6.5l3.5 3.5-3.5 3.5"/>
  </g>
</svg>

<div class="abs service-card" style="left:39px">
  <div class="service-photo" role="img" aria-label="Workers in hard hats reviewing a building under construction" style="background:linear-gradient(#3c5d8f,#8a9fb6 55%,#7d8a3c)"></div>
  <div class="service-label">PROJECT MANAGEMENT</div>
</div>
<div class="abs service-card" style="left:217px">
  <div class="service-photo" role="img" aria-label="Engineer in orange hard hat pointing at plant equipment" style="background:linear-gradient(120deg,#c9cdd2,#9aa3ab 55%,#2b2b2b)"></div>
  <div class="service-label">ENGINEERING SERVICES</div>
</div>
<div class="abs service-card" style="left:397px">
  <div class="service-photo" role="img" aria-label="Construction worker in yellow hard hat on a building site" style="background:linear-gradient(#7d8c9a,#b9bdbf 50%,#6e6a5f)"></div>
  <div class="service-label">CONSTRUCTION</div>
</div>
<div class="abs service-card" style="left:577px">
  <div class="service-photo" role="img" aria-label="Orange industrial robots on an automated assembly line" style="background:linear-gradient(#8f8f8f,#c6c3bf 55%,#b06a3a)"></div>
  <div class="service-label">AUTOMATION</div>
</div>

<h2 class="abs section-title testimonial-title">Customer Testimonial</h2>
<svg class="abs quote-mark" width="28" height="22" viewBox="0 0 30 24" aria-hidden="true">
  <g fill="#c8c8c8"><circle cx="7" cy="16" r="7"/><path d="M1 15C1 7 5 2 12 1l1 3C8 5 6 9 6 13z"/><circle cx="22" cy="16" r="7"/><path d="M16 15c0-8 4-13 11-14l1 3c-5 1-7 5-7 9z"/></g>
</svg>
<p class="abs testimonial-text">Nemo enim ipsam voluptatem quia voluptas sit aspernatur aut odit aut fugit, sed quia consequuntur magni dolores eos qui ratione voluptatem sequi nesciunt. Neque porro quisquam est, qui dolorem ipsum quia dolor sit amet, consectetur, adipisci velit, sed quia non numquam eius modi tempora incidunt ut labore et dolore magnam aliquam quaerat voluptatem.</p>
<p class="abs testimonial-author">- Lorem ipsum dolor -</p>

<div class="abs rule-thick"></div>

<footer>
  <h3 class="abs footer-heading" style="left:40px">SERVICES</h3>
  <ul class="abs footer-list" style="left:39px">
    <li>Project Management</li><li>Procurement</li><li>Engineering Services</li><li>Construction</li><li>Controls and Automation</li>
  </ul>
  <ul class="abs footer-list" style="left:207px">
    <li>Field Services</li><li>Industries</li><li>Technical Expertise</li><li>System Expertise</li>
  </ul>
  <h3 class="abs footer-heading" style="left:337px">OUR AREAS</h3>
  <ul class="abs footer-list" style="left:338px">
    <li>Field Services</li><li>Industries</li><li>Technical Expertise</li><li>System Expertise</li>
  </ul>
  <h3 class="abs footer-heading" style="left:474px">CONTACT</h3>
  <p class="abs contact-text">Nemo enim ipsam voluptatem quia voluptas sit</p>
  <p class="abs contact-phone">1800-555-019</p>
  <h3 class="abs footer-heading" style="left:659px">FOLLOW US</h3>
  <ul class="abs social">
    <li><i></i>Chatterly</li><li><i></i>Postwave</li><li><i></i>RSS</li>
  </ul>

  <div class="abs rule-thin"></div>
  <nav class="abs footer-nav">
    <a>Home</a><a>Services</a><a>Products</a><a>Equipment</a><a>News</a><a>About us</a><a>Contact us</a><a>Remote Support</a>
  </nav>
  <p class="abs copyright">ridgelinevantek.example © 2015 Privacy Policy</p>
</footer>

</body>
</html>
```